770 76 Chiro Brochure

https://files.brindlewick.net/papers/p/58KqWz_rMa-Tn_XcLpQe913vhD7tYRfNBwKsGu2Jx6/view?mode=shared

Brochure to show chiropractors about our program

```html
<!DOCTYPE html>
<html lang="en">
<head>
<meta charset="utf-8">
<title>Chiropractic Billboard Program Brochure</title>
<link rel="stylesheet" href="https://fonts.googleapis.com/css2?family=Oswald:wght@500;700&family=Lato:wght@400;700&family=Anton&display=swap">
<style>
  :root {
    --navy: #2b3d8f;
    --band: #33479c;
    --ink-blue: #2d3f95;
    --yellow: #f7c81e;
    --white: #ffffff;
    --text: #2a2a2a;
    --red: #e3262b;
    --ad-dark: #0f1a12;
    --ad-green: #1d3a22;
    --page: #e9e9ec;
  }
  * { margin: 0; padding: 0; box-sizing: border-box; }
  html, body { width: 1200px; height: 801px; overflow: hidden; background: var(--page); }
  body { position: relative; font-family: "Lato", sans-serif; }

  .brochure {
    position: absolute; left: 294px; top: 5px; width: 612px; height: 790px;
    background: var(--white); overflow: hidden;
    box-shadow: 0 2px 10px rgba(0,0,0,.18);
  }
  .backdrop { position: absolute; inset: 0; }

  .hero-title {
    position: absolute; left: 21px; top: 62px;
    font-family: "Oswald", sans-serif; font-weight: 700; color: var(--white);
    font-size: 27px; line-height: 33px; letter-spacing: .2px;
  }
  .tag-pill {
    position: absolute; left: 19px; top: 140px; width: 206px; height: 28px;
    background: var(--yellow); border-radius: 14px;
    font-family: "Oswald", sans-serif; font-weight: 500; color: var(--ink-blue);
    font-size: 17px; line-height: 28px; text-align: center;
  }
  .partner-line {
    position: absolute; left: 19px; top: 184px; color: var(--white); font-size: 14px;
  }
  .site-link {
    position: absolute; left: 22px; top: 206px; color: var(--yellow);
    font-size: 12px; font-weight: 700; display: flex; align-items: center; gap: 7px;
  }
  .site-link .dot { width: 10px; height: 10px; border-radius: 50%; background: var(--yellow); }

  .dominate {
    position: absolute; left: 31px; top: 280px; width: 540px; color: var(--white);
  }
  .dominate h2 { font-size: 13px; font-weight: 700; letter-spacing: .1px; margin-bottom: 14px; }
  .dominate li {
    list-style: none; position: relative; padding-left: 28px; font-size: 10px;
    line-height: 13px; margin-bottom: 13px;
  }
  .dominate li svg { position: absolute; left: 0; top: 0; }

  .includes { position: absolute; left: 21px; top: 453px; width: 282px; }
  .section-head {
    font-family: "Oswald", sans-serif; font-weight: 500; color: var(--ink-blue);
    font-size: 13px; line-height: 15px;
  }
  .includes ul { margin: 7px 0 0 10px; }
  .includes li { font-size: 10.5px; line-height: 13px; color: var(--text); list-style: none; position: relative; }
  .includes li::before {
    content: ""; position: absolute; left: -9px; top: 5px; width: 4px; height: 4px;
    border-radius: 50%; background: var(--ink-blue);
  }
  .reach { position: absolute; left: 19px; top: 535px; width: 282px; }
  .reach p {
    font-size: 8.6px; line-height: 12px; color: var(--text); text-align: justify; margin-top: 4px;
  }
  .reach p + p { margin-top: 11px; }

  .locations { position: absolute; left: 313px; top: 453px; width: 285px; }
  .locations .section-head { font-size: 12.5px; }
  .city-grid { display: flex; gap: 0; margin-top: 10px; }
  .city-grid ul { list-style: none; width: 92px; }
  .city-grid li { font-size: 8.4px; line-height: 10px; color: var(--text); }
  .city-grid li::before { content: "· "; }

  .ad-banner {
    position: absolute; top: 660px; width: 280px; height: 98px;
    background: linear-gradient(100deg, var(--ad-dark) 0%, var(--ad-green) 100%);
    overflow: hidden; color: var(--white);
  }
  .ad-banner.left { left: 21px; }
  .ad-banner.right { left: 313px; }
  .ad-photo {
    position: absolute; right: 0; top: 0; width: 80px; height: 98px;
    background: linear-gradient(180deg, #4a4aa0 0%, #2c2c6e 100%);
  }
  .ad-banner.right .ad-photo { background: linear-gradient(180deg, #d9d9d9 0%, #8a8a8a 100%); }
  .ad-injured {
    position: absolute; left: 7px; top: 5px; font-family: "Anton", sans-serif;
    font-size: 20px; line-height: 22px; color: var(--red);
  }
  .ad-injured span { color: var(--yellow); font-family: "Oswald", sans-serif; font-weight: 700; font-size: 12px; }
  .ad-call {
    position: absolute; left: 7px; top: 32px; font-family: "Oswald", sans-serif; font-weight: 700;
    color: var(--yellow); font-size: 11px; line-height: 10px;
  }
  .ad-phone {
    position: absolute; left: 42px; top: 27px; font-family: "Anton", sans-serif;
    font-size: 24px; line-height: 28px; color: var(--white);
  }
  .ad-small { position: absolute; left: 7px; top: 57px; font-size: 6.2px; letter-spacing: .2px; }
  .ad-pill {
    position: absolute; top: 68px; height: 14px; padding: 0 9px; background: var(--yellow);
    color: #15180f; font-weight: 700; font-size: 10px; line-height: 14px; border-radius: 7px 0 0 7px;
  }
  .ad-banner.left .ad-pill { left: 74px; }
  .ad-banner.right .ad-pill { left: 79px; top: 74px; }
  .ad-brand { position: absolute; left: 8px; bottom: 6px; font-size: 12px; font-weight: 700; display: flex; align-items: center; gap: 4px; }
  .ad-brand .mark { width: 9px; height: 9px; background: var(--white); border-radius: 50%; }
  .ad-doctors { position: absolute; left: 74px; bottom: 5px; font-size: 5px; font-weight: 700; }
</style>
</head>
<body>
  <main class="brochure">
    <svg class="backdrop" width="612" height="790" viewBox="0 0 612 790" aria-hidden="true">
      <defs>
        <linearGradient id="sky" x1="0" y1="0" x2="0" y2="1">
          <stop offset="0" stop-color="#3b8fd6"/>
          <stop offset="1" stop-color="#bfe0f5"/>
        </linearGradient>
      </defs>
      <rect x="0" y="0" width="612" height="260" fill="var(--navy)"/>
      <polygon points="0,252 318,252 612,238 612,452 0,410" fill="var(--band)"/>
      <rect x="0" y="772" width="612" height="18" fill="var(--navy)"/>
    </svg>

    <svg style="position:absolute;left:0;top:0" width="612" height="260" viewBox="0 0 612 260"
         role="img" aria-label="Photo of a roadside billboard advertising the vanity phone number against a blue sky">
      <polygon points="245,0 612,0 612,238 318,252" fill="url(#sky)"/>
    </svg>

    <h1 class="hero-title">CHIROPRACTIC<br>BILLBOARD PROGRAM</h1>
    <div class="tag-pill">PERSONAL INJURY</div>
    <p class="partner-line">We Partner With Georgia Chiropractors</p>
    <p class="site-link"><span class="dot"></span>www.spineboardsga.com</p>

    <section class="dominate">
      <h2>HOW TO DOMINATE PERSONAL INJURY ADVERTISING</h2>
      <ul>
        <li><svg width="18" height="18" viewBox="0 0 18 18"><circle cx="9" cy="9" r="9" fill="var(--yellow)"/><path d="M5 9.3l2.6 2.6L13 6.5" stroke="var(--navy)" stroke-width="2" fill="none"/></svg>(555) 24-SPINE is the preeminent vanity phone number for Chiropractors in Georgia to dominate personal injury advertising.</li>
        <li><svg width="18" height="18" viewBox="0 0 18 18"><circle cx="9" cy="9" r="9" fill="var(--yellow)"/><path d="M5 9.3l2.6 2.6L13 6.5" stroke="var(--navy)" stroke-width="2" fill="none"/></svg>(555) 24-SPINE is more valuable than ever because of digital advertising.</li>
        <li><svg width="18" height="18" viewBox="0 0 18 18"><circle cx="9" cy="9" r="9" fill="var(--yellow)"/><path d="M5 9.3l2.6 2.6L13 6.5" stroke="var(--navy)" stroke-width="2" fill="none"/></svg>See how (555) 24-SPINE proved to substantially increase ROI through the Searchly Ads Algorithm and increase your Searchly Quality Score.</li>
      </ul>
    </section>

    <section class="includes">
      <h3 class="section-head">EVERY BILLBOARD WE CREATE INCLUDES</h3>
      <ul>
        <li>Doctors Photo</li>
        <li>Your Brand / Logo on the billboards</li>
        <li>Direct dial forwarded to your office</li>
      </ul>
    </section>

    <section class="reach">
      <h3 class="section-head">Reach New Clients / Patients in a Big Way!</h3>
      <p>Expand your marketing mix and grow your business through our professionally designed billboards that showcase your photo, name, logo, at any time and in any place.</p>
      <p>Billboards set you apart from the competition by building credibility and brand recognition. Billboards serve as an important top-of-funnel channel and in conjunction with your current marketing channels, will increase your effectiveness.</p>
    </section>

    <section class="locations">
      <h3 class="section-head">Georgia Billboard Locations<br>&nbsp;(Over 200 Boards Available)</h3>
      <div class="city-grid">
        <ul><li>Albany</li><li>Athens</li><li>Atlanta</li><li>Augusta</li><li>Blairsville</li><li>Blackshear</li><li>Blue Ridge</li><li>Conyers</li><li>Valdosta</li><li>Cummings</li><li>Dalton</li><li>Ft Oglethorpe</li><li>Hazelhurst</li><li>Jesup</li><li>Kennesaw</li></ul>
        <ul><li>Macon</li><li>McDonough</li><li>Savannah</li><li>Thomasville</li><li>Toccoa</li><li>Young Harris</li><li>Watkinsville</li><li>Bogart</li><li>Winder</li><li>Sandersville</li><li>Tifton</li><li>Cordele</li><li>Clayton</li><li>Milledgeville</li><li>Dublin</li></ul>
        <ul><li>Chatsworth</li><li>Mineral Bluff</li><li>Eatonsville</li><li>Hinesville</li><li>Warner Robins</li><li>Moultrie</li><li>LaFayette</li><li>Senoia</li><li>Ackworth</li><li>Camilla</li><li>Dawsonville</li><li>Barnesville</li><li>Bainbridge</li><li>Cairo</li><li>Americus</li></ul>
      </div>
    </section>

    <div class="ad-banner left">
      <div class="ad-photo" role="img" aria-label="Photo of two chiropractors in scrubs"></div>
      <p class="ad-injured">INJURED <span>IN A CAR ACCIDENT?</span></p>
      <p class="ad-call">CALL<br>NOW</p>
      <p class="ad-phone">(555) 24-SPINE</p>
      <p class="ad-small">SAME DAY APPOINTMENTS | LOCATIONS ACROSS GEORGIA</p>
      <p class="ad-pill">NECK &amp; BACK PAIN</p>
      <p class="ad-brand"><span class="mark"></span>Oakline Spine</p>
      <p class="ad-doctors">DR. LENA MARSH, D.C &amp; DR. OWEN PRATT, D.C</p>
    </div>

    <div class="ad-banner right">
      <div class="ad-photo" role="img" aria-label="Photo of a chiropractor in a white coat"></div>
      <p class="ad-injured">INJURED <span>IN A CAR ACCIDENT?</span></p>
      <p class="ad-call">CALL<br>NOW</p>
      <p class="ad-phone">(555) 24-SPINE</p>
      <p class="ad-small">SAME DAY APPOINTMENTS | LOCATIONS ACROSS GEORGIA</p>
      <p class="ad-pill">NECK &amp; BACK PAIN</p>
      <p class="ad-brand" style="font-size:9px"><span class="mark"></span>Birchway Care</p>
    </div>
  </main>
</body>
</html>
```